Dive Bar/ Pop Culture Bar Adult Nugget Night

Hey guys,
Gareth here from Rusty Clems restaurant in Australia. Im after a poster design for our new Monday Night Special - Adult Nugget Night. - Think crumbed chicken or Beef Schnitzel with different toppings like Philly Cheese steak or Cheese burger smash (aka a parmy).

I'm thinking a plain block blue colour background with a vector image as the main focus - see attached graphics. I would like the poster to be a fun and tongue in cheek and a 80's/90's hip hop vibe and vector image of a nugget "thug life".

The info it has to contain are as follows -
- Adult Nugget Night (title)
- Monday Night
- Price $17
- from 5pm

Toppings
- Philly Cheese Steak
- Cheese burger Smash
- Burnt End Beanz

A little about Rusty Clems
-Rusty Clems came about because we fell in love with the old- skool American south culture of slow cooked soul food, thrown together on big hearty share plates in the backyard and tucked into with the ones you love.

We wanted to bring something different to the coast.

Moody and grungy without losing the soul of why we go out to drink and eat in the first place - to fill our bellies and warm our hearts.

That's why communal eating is at the core of what we do. Low 'n' Slow platters of scrumptious, fall off the bone meat. Sided with delicious dishes of your choice. That quietness that falls on the table as everyone savours the flavours. Laughs as you reach across your mate, to fork that last juicy piece of slow cooked meat that someone else was eyeing off. Washing it all down with hand-crafted beer, or better yet, that top shelf whiskey glistening from the back bar. Finishing off the night with the best kind of dessert.. our famous Sticky Date Espresso Martini!

I have found one image on the net that I like....... don't know if it's useful...

Please reach out for any more info or questions needed

Cheers
Gareth

Target Market(s)

20-40 year old for a funky grudge bar

Industry/Entity Type

Dive Bar, Smokehouse, Bar & Grill

Font styles to use
Other font styles liked:
• Veneer

Colors
0054AA
0677BA
7BADD7
CADEEF
E8F1F8
FFF300
FFF600
FEFA6F
FFFEC7
FFFEE8
F0912C
F2A743
F7CA91
FBE8D2
FDF5EE
EB3D1F
EC4F4E
F09395
F8D3D4
FCEDEE

Requirements
Must have
• Business Name "Rusty Clems" will share Logo in later stages
Nice to have
• Nice bold colours which throw back to 1980/90's pop culture

```html
<!DOCTYPE html>
<html lang="en">
<head>
<meta charset="utf-8">
<title>Adult Nugget Night – Rusty Clems</title>
<link rel="stylesheet" href="https://fonts.googleapis.com/css2?family=Bebas+Neue&family=Montserrat:wght@400;800&display=swap">
<style>
  :root {
    --ink: #2f2d2d;
    --ink-edge: #4a4747;
    --red: #e8392a;
    --cream: #f8f2dc;
    --gold: #f2a743;
    --nugget: #f0912c;
    --nugget-light: #f7ca91;
    --white: #ffffff;
  }
  * { box-sizing: border-box; margin: 0; padding: 0; }
  html, body { width: 750px; height: 1200px; overflow: hidden; background: var(--ink); }
  .poster {
    position: relative;
    width: 750px; height: 1200px; overflow: hidden;
    background: radial-gradient(ellipse at center, var(--ink) 70%, var(--ink-edge) 100%);
    font-family: "Bebas Neue", "Arial Narrow", sans-serif;
  }
  .hero-art {
    position: absolute; left: 400px; top: 0; width: 350px; height: 960px;
    background: radial-gradient(ellipse at 60% 45%, var(--nugget-light) 0%, var(--nugget) 45%, rgba(240,145,44,0) 75%);
    opacity: .85;
  }
  .title { position: absolute; left: 62px; top: 72px; line-height: .82; z-index: 2; }
  .title span { display: block; font-size: 176px; }
  .title .red { color: var(--red); }
  .title .cream { color: var(--cream); margin: 10px 0 8px; }
  .offer { position: absolute; left: 62px; top: 552px; z-index: 2; }
  .offer .day { color: var(--cream); font-size: 60px; line-height: .88; }
  .offer .price { color: var(--gold); font-size: 124px; line-height: .9; margin-top: 6px; }
  .offer .price sup { font-size: 58px; vertical-align: 44px; }
  .offer .time {
    display: inline-block; margin-top: 8px; padding: 3px 10px 0;
    background: var(--red); color: var(--white); font-size: 34px; border-radius: 3px;
  }
  .brand {
    position: absolute; left: 62px; top: 920px; width: 150px;
    color: var(--cream); font-size: 76px; line-height: .9; text-align: center;
  }
  .toppings { position: absolute; left: 253px; top: 890px; width: 440px; }
  .toppings h2 { color: var(--gold); font-weight: 400; font-size: 44px; line-height: 1; margin-bottom: 12px; }
  .toppings ul { list-style: none; }
  .toppings li {
    display: flex; align-items: center; gap: 6px; height: 29px;
    font-family: "Montserrat", sans-serif; font-weight: 800; font-size: 17px; color: var(--cream);
  }
  .toppings li svg { width: 20px; height: 20px; flex: none; }
  .about {
    margin-top: 30px; font-family: "Montserrat", sans-serif; font-size: 13.4px;
    line-height: 17px; color: var(--white);
  }
</style>
</head>
<body>
<main class="poster">
  <div class="hero-art" role="img" aria-label="Illustration of crispy chicken nuggets tumbling into a red and cream nugget bucket"></div>

  <h1 class="title">
    <span class="red">Adult</span>
    <span class="cream">Nugget</span>
    <span class="red">Night</span>
  </h1>

  <section class="offer">
    <p class="day">Monday<br>Night</p>
    <p class="price"><sup>$</sup>17</p>
    <p class="time">From 5PM</p>
  </section>

  <p class="brand">Rusty<br>Clems</p>

  <section class="toppings">
    <h2>Toppings</h2>
    <ul>
      <li><svg viewBox="0 0 20 20"><path d="M2 11l5 5L18 3" fill="none" stroke="#e8392a" stroke-width="3" stroke-linecap="round"/></svg>PHILLY CHEESE STEAK</li>
      <li><svg viewBox="0 0 20 20"><path d="M2 11l5 5L18 3" fill="none" stroke="#e8392a" stroke-width="3" stroke-linecap="round"/></svg>CHEESE BURGER SMASH</li>
      <li><svg viewBox="0 0 20 20"><path d="M2 11l5 5L18 3" fill="none" stroke="#e8392a" stroke-width="3" stroke-linecap="round"/></svg>BURNT END BEANZ</li>
    </ul>
    <p class="about">Rusty Clems came about because we fell in love with the old skool American south culture of slow cooked soul food, thrown together on big hearty share plates in the backyard and tucked into with the ones you love.</p>
  </section>
</main>
</body>
</html>
```